Broschüre für Energieberater
Zielgruppe
Unternehmen die zu den KMU´s gehören (kleine und mittlere Unternehmen) haben die Möglichkeit eine Energieberatung über die ZEKV fördern zu lassen. Diese Beratung wird durch unsere Ingenieure durchgeführt und ist für den Kunden völlig kostenneutral. Zum einen erhält er eine 80% Förderung von der ZEKV (Zentralstelle für Kostenausgleich und Versorgung) die restlichen 20% erhält der Kunde von uns als Gutschrift. Wir finanzieren uns somit nur über die Fördergelder des Bundes. Die Vorteile des Kunden sind: Verringerung von Steuern, Einsparung von mindestens 10% an Energie ohne zusätzliche Kosten und somit weniger C0² Ausstoss, was wiederum allen zugute kommt. Somit ein hohes Maß an Umweltbewusstsein! Alle Investitionen die für die Einsparung von Energie von Vorteil sind, werden vom Bund mit bis zu 200.000 Euro gefördert. Voraussetzung eine durchgeführte ZEKV Energieberatung. Somit eine win/win Situation für alle Beteiligten.
Aufgabenstellung
Das Design kann - muss - nicht an unsere Webseite : www.wattlinde-beratung.de angelehnt sein.

```html
<!DOCTYPE html>
<html lang="de">
<head>
<meta charset="utf-8">
<title>Broschüre Energieberatung</title>
<link href="https://fonts.googleapis.com/css2?family=Barlow+Condensed:wght@500;600&family=Arimo:wght@400&display=swap" rel="stylesheet">
<style>
  :root {
    --yellow: #e6cd22;
    --black: #121212;
    --white: #f7f7f5;
    --grass-dark: #2c4418;
    --grass-mid: #4a6d2a;
    --grass-light: #6c8f3e;
    --text: #1a1a1a;
  }
  * { margin: 0; padding: 0; box-sizing: border-box; }
  html, body { width: 1200px; height: 801px; overflow: hidden; background: #ffffff; }
  .brochure { position: relative; width: 1200px; height: 801px; overflow: hidden; }

  .photo-grass {
    position: absolute; left: 0; top: 0; width: 800px; height: 690px;
    background: radial-gradient(ellipse at 58% 38%, #cfccc4 0 14%, transparent 15%),
                linear-gradient(160deg, var(--grass-light), var(--grass-mid) 45%, var(--grass-dark));
  }
  .fold-accent { position: absolute; left: 372px; top: 90px; width: 52px; height: 600px; background: var(--yellow); }

  .intro-card {
    position: absolute; left: 28px; top: 44px; width: 344px; height: 560px;
    background: var(--white); padding: 48px 34px 30px 40px;
  }
  .intro-card h2 {
    font-family: "Barlow Condensed", sans-serif; font-weight: 600;
    font-size: 50px; line-height: 0.95; color: var(--text); margin-bottom: 30px;
  }
  .intro-card p {
    font-family: "Arimo", sans-serif; font-size: 14px; line-height: 1.42; color: var(--text);
  }

  .contact-band {
    position: absolute; left: 0; top: 690px; width: 800px; height: 111px;
    background: var(--black); display: flex; align-items: center; justify-content: center;
    font-family: "Barlow Condensed", sans-serif; font-weight: 600; font-size: 32px; color: var(--white);
  }
  .contact-band .url { color: var(--yellow); margin-left: 8px; }

  .cover { position: absolute; left: 800px; top: 0; width: 400px; height: 801px; background: var(--yellow); }
  .cover h1 {
    position: absolute; left: 48px; top: 48px;
    font-family: "Barlow Condensed", sans-serif; font-weight: 600;
    font-size: 44px; line-height: 1.35; color: var(--text);
  }
  .brand { position: absolute; left: 72px; top: 212px; display: flex; align-items: center; gap: 8px; }
  .brand-dot { width: 14px; height: 14px; background: var(--text); }
  .brand-name { font-family: "Barlow Condensed", sans-serif; font-weight: 600; font-size: 30px; color: var(--text); }

  .photo-bulb {
    position: absolute; left: 80px; top: 270px; width: 320px; height: 200px;
    background: radial-gradient(circle at 42% 55%, #ffffff 0 12%, #ececea 13%, #dcdcd8);
  }
  .savings-card {
    position: absolute; left: 188px; top: 450px; width: 200px; height: 180px;
    background: var(--white); padding: 24px 22px;
    font-family: "Barlow Condensed", sans-serif; font-weight: 500; color: var(--text);
    font-size: 34px; line-height: 1.15;
  }
  .savings-card .value { color: var(--yellow); font-size: 52px; line-height: 1.1; }
  .cover-rule { position: absolute; left: 0; top: 630px; width: 400px; height: 10px; background: var(--black); }
  .photo-grass-cover {
    position: absolute; left: 0; top: 640px; width: 400px; height: 161px;
    background: linear-gradient(170deg, var(--grass-light), var(--grass-mid) 50%, var(--grass-dark));
  }
</style>
</head>
<body>
<main class="brochure">
  <div class="photo-grass" role="img" aria-label="Foto: weiße Steckdose auf grüner Rasenfläche"></div>
  <div class="fold-accent"></div>

  <section class="intro-card">
    <h2>Effizient Energie sparen</h2>
    <p>Eine effizientere Nutzung der Energie zu erreichen, bedeutet nicht gleichzeitig immer größere Investitionen tätigen zu müssen. Bereits durch die Optimierung bestehender Betriebsprozesse können erhebliche Energiekostenreduzierungen erreicht werden. Dies ist für Sie somit völlig kostenneutral! Durch eine geförderte Energieberatung erhalten Sie bei minimalem eigenem Aufwand einen maximalen Überblick über den aktuellen Energieverbrauch in Ihrem Unternehmen, sowie konkrete Vorschläge und betriebswirtschaftliche Berechnungen für Maßnahmen zur Optimierung Ihres Energieverbrauchs!</p>
  </section>

  <footer class="contact-band">
    Wir beraten Sie auch online unter <span class="url">www.wattlinde-beratung.de.</span>
  </footer>

  <section class="cover">
    <h1>Energie sparen<br>heißt Geld sparen</h1>
    <div class="brand"><span class="brand-dot"></span><span class="brand-name">Wattlinde</span></div>
    <div class="photo-bulb" role="img" aria-label="Foto: Energiesparlampe auf weißem Grund mit gelben Strahlen"></div>
    <div class="savings-card">Sparen Sie<br>bis zu<br><span class="value">25%</span></div>
    <div class="cover-rule"></div>
    <div class="photo-grass-cover" role="img" aria-label="Foto: grüne Rasenfläche"></div>
  </section>
</main>
</body>
</html>
```